Business card - KT Talent Advisors / The Marlow Group

We need a business card and logo design for my executive search (recruiting / headhunting) firm. We find people to fill open jobs at companies. We are a U.S. based company and do some global work also. So maybe something with a globe but definitely looking for other options also. Maybe something incorporating the letters KT which is our current logo but looking at options. The card should say BOTH full company names and tag line-

KT Talent Advisors / The Marlow Group
Leadership Placement You Can Rely On

The design should say about the company-
Sharp
Reliable
Find the best people for the job
Business oriented
Results achieved
Modern

Target Market(s)

Business owners, CEO's, and heads of human resources departments

Industry/Entity Type

Business Consultant

Contact Information for Business Card

The card MUST say BOTH full company names and tag line-

Logo Text

Logo does not NEED to say anything on the design itself, but could if designed that way.

Font styles to use
Serif
Sans Serif

Requirements
Must have
• The business cards need to have. In addition to name, title, address, phone, website, and email address,
• The card MUST say BOTH full company names and tag line-
• KT Talent Advisors / The Marlow Group
• Leadership Placement You Can Rely On
Nice to have
• The design should say about the company-
• Sharp
• Reliable
• Find the best people for the job
• Business oriented
• Results achieved
• Modern
• Maybe something with a globe or the letters KT or relating to people. Open to options.
Should not have
• Should not be cutesy or funny, for this design

```html
<!DOCTYPE html>
<html lang="en">
<head>
<meta charset="utf-8">
<title>KT Talent Advisors – Business Card</title>
<link rel="stylesheet" href="https://fonts.googleapis.com/css2?family=Lato:wght@400;700&display=swap">
<style>
  :root {
    --backdrop: #5f5f5f;
    --card: #ffffff;
    --card-edge: #1a1a1a;
    --navy: #0f4a7c;
    --slate: #4a4f57;
    --ink: #1c1c1c;
    --map-tint: #e3e7ee;
    --map-fade: #f4f6f9;
  }
  * { margin: 0; padding: 0; box-sizing: border-box; }
  html, body {
    width: 1200px; height: 921px; overflow: hidden;
    background: var(--backdrop);
  }
  .card {
    position: absolute; left: 50px; top: 139px;
    width: 1100px; height: 643px;
    background: var(--card);
    border: 2px solid var(--card-edge);
    font-family: "Lato", sans-serif;
    color: var(--ink);
  }
  .world-map {
    position: absolute; left: 78px; top: 150px;
    width: 980px; height: 280px;
    background: radial-gradient(ellipse at center, var(--map-tint) 0%, var(--map-fade) 60%, var(--card) 100%);
    border-radius: 40px;
  }
  .brand {
    position: absolute; left: 219px; top: 80px;
    display: flex; align-items: center; gap: 24px;
  }
  .brand-mark { width: 56px; height: 56px; background: var(--navy); flex: none; }
  .brand-name {
    font-family: "Lato", sans-serif; font-weight: 400;
    font-size: 46px; color: var(--navy); white-space: nowrap;
  }
  .person { position: absolute; right: 78px; top: 262px; text-align: right; }
  .person-name { font-size: 34px; color: var(--slate); line-height: 1.15; }
  .person-title { font-size: 24px; font-weight: 700; line-height: 1.3; }
  .rule {
    position: absolute; left: 82px; top: 358px;
    width: 942px; height: 4px; background: var(--ink);
  }
  .contact { position: absolute; left: 82px; top: 382px; list-style: none; }
  .contact li {
    display: flex; align-items: center; gap: 14px;
    height: 44px; font-size: 27px; color: var(--ink);
  }
  .contact .address { padding-left: 4px; }
  .contact svg { width: 28px; height: 28px; flex: none; }
  .tagline {
    position: absolute; left: 0; right: 0; top: 566px; text-align: center;
    font-family: "Lato", sans-serif; font-weight: 700;
    font-size: 27px; letter-spacing: 0.04em; color: var(--navy);
  }
</style>
</head>
<body>
  <article class="card">
    <div class="world-map" role="img" aria-label="Faint dotted world map in light grey and blue"></div>

    <header class="brand">
      <span class="brand-mark"></span>
      <span class="brand-name">KT Talent Advisors</span>
    </header>

    <div class="person">
      <div class="person-name">Daniel C. Marlow</div>
      <div class="person-title">President, The Marlow Group</div>
    </div>

    <div class="rule"></div>

    <ul class="contact">
      <li class="address">4570 Cedar Crest Ln. Tampa, FL 33602</li>
      <li>
        <svg viewBox="0 0 24 24" aria-hidden="true"><path fill="#1c1c1c" d="M2 8c0-3 4-5 10-5s10 2 10 5v2h-5V8H7v2H2zM5 12h14l2 8H3z"/><circle cx="12" cy="16" r="2.2" fill="#fff"/></svg>
        <span>555-013-4200</span>
      </li>
      <li>
        <svg viewBox="0 0 24 24" aria-hidden="true"><rect x="2" y="5" width="20" height="14" fill="#1c1c1c"/><path d="M3 6l9 7 9-7" fill="none" stroke="#fff" stroke-width="1.6"/></svg>
        <span>danielm@kttalentadvisors.com</span>
      </li>
      <li>
        <svg viewBox="0 0 24 24" aria-hidden="true"><g fill="none" stroke="#1c1c1c" stroke-width="2"><rect x="3" y="11" width="10" height="6" rx="3" transform="rotate(-45 8 14)"/><rect x="11" y="7" width="10" height="6" rx="3" transform="rotate(-45 16 10)"/></g></svg>
        <span>www.kttalentadvisors.com</span>
      </li>
    </ul>

    <p class="tagline">Leadership Placement You Can Rely On</p>
  </article>
</body>
</html>
```